Painting Valtoni Renovations New buildings

Paint jobs plasterwork renovations new building customer painter paper drywall Entsorgungen.neukunden win color splash pleasure in colors competent clean fast reliable new try build demolition color combinations color concepts offers washing façade painting wood stains new projects old building renovations yes no beautiful new old sell secure solve paint over paint paint spray paint lye assemble disassemble sell buy trade oil dust new old assembly disassembly putty sanding fashion devastation copying belief feng shui kleopatra pompes beer colors swamp lime abrasion release tighten

Target Market(s)

construction industry

Contact Information for Business Card

Maler

Font styles to use
Serif

Colors
f04a50
959595

Requirements
Must have
• elegant appearance
Nice to have
• simply goal-oriented clientele in detail
Should not have
• too colorful

```html
<!DOCTYPE html>
<html lang="en">
<head>
<meta charset="UTF-8">
<title>Merenda Valtoni – Business Card</title>
<link href="https://fonts.googleapis.com/css2?family=Lato:wght@400;700&display=swap" rel="stylesheet">
<style>
  :root {
    --card-blue: #1f457c;
    --text-white: #ffffff;
    --page-bg: #e9e9ea;
    --badge-light: #f4f4f4;
    --badge-shade: #e2e2e3;
    --brand-blue: #24407e;
  }
  html, body {
    margin: 0;
    width: 1200px;
    height: 900px;
    overflow: hidden;
    background: var(--page-bg);
    font-family: "Lato", Arial, sans-serif;
  }
  .card {
    position: absolute;
    left: 150px;
    top: 172px;
    width: 900px;
    height: 556px;
    background: var(--card-blue);
    color: var(--text-white);
    box-shadow: 0 10px 30px rgba(0,0,0,0.18);
  }
  .holder-name {
    position: absolute;
    left: 52px;
    top: 56px;
    margin: 0;
    font-size: 31px;
    font-weight: 700;
    letter-spacing: 0.2px;
    text-transform: uppercase;
    line-height: 1;
  }
  .holder-role {
    position: absolute;
    left: 52px;
    top: 94px;
    margin: 0;
    font-size: 24px;
    font-weight: 400;
    line-height: 1;
  }
  .contact-list {
    position: absolute;
    left: 50px;
    top: 304px;
    margin: 0;
    padding: 0;
    list-style: none;
    font-size: 24px;
    line-height: 32.5px;
  }
  .contact-list li {
    display: flex;
    align-items: center;
    gap: 8px;
  }
  .contact-icon {
    width: 20px;
    height: 20px;
    fill: var(--text-white);
  }
  .address {
    position: absolute;
    left: 55px;
    top: 428px;
    margin: 0;
    font-size: 24px;
    line-height: 32px;
    font-style: normal;
  }
  .brand-badge {
    position: absolute;
    left: 371px;
    top: 39px;
    width: 480px;
    height: 480px;
    border-radius: 50%;
    background: radial-gradient(circle at 45% 40%, var(--badge-light) 0%, var(--badge-shade) 100%);
    display: flex;
    align-items: center;
    justify-content: center;
  }
  .brand-name {
    font-size: 68px;
    font-weight: 700;
    color: var(--brand-blue);
    letter-spacing: 1px;
  }
</style>
</head>
<body>
  <section class="card">
    <h1 class="holder-name">Merenda Valtoni</h1>
    <p class="holder-role">Managing Director</p>

    <ul class="contact-list">
      <li>
        <svg class="contact-icon" viewBox="0 0 24 24" aria-hidden="true">
          <path d="M3 9c0-2 4-4 9-4s9 2 9 4l-1 2-4-1-1-2c-2-.5-4-.5-6 0l-1 2-4 1zM6 13h12l1 6H5z"/>
        </svg>
        044-123 456 789
      </li>
      <li>
        <svg class="contact-icon" viewBox="0 0 24 24" aria-hidden="true">
          <path d="M3 6h18v12H3z M3 6l9 7 9-7" fill="none" stroke="#fff" stroke-width="2"/>
          <rect x="3" y="6" width="18" height="12"/>
          <path d="M3 6l9 7 9-7" fill="none" stroke="#1f457c" stroke-width="1.8"/>
        </svg>
        info@webname.com
      </li>
      <li>
        <svg class="contact-icon" viewBox="0 0 24 24" aria-hidden="true">
          <circle cx="12" cy="12" r="10"/>
          <path d="M7 8c2 0 3 1 3 3s-2 2-2 4 1 3 1 4M15 5c0 2 2 2 2 4s-2 2-2 4" fill="none" stroke="#1f457c" stroke-width="1.8"/>
        </svg>
        www.websitename.com
      </li>
    </ul>

    <address class="address">
      421, Address line here,<br>
      45452,Country Name
    </address>

    <div class="brand-badge">
      <span class="brand-name">Corvello</span>
    </div>
  </section>
</body>
</html>
```